QM Studios needs and Interior Design Business card

I can do anything from Commercial to Residential and Free lance. Beginning to end in design selection process.
Need something to catch the eye of potential customers and vendors. From furniture to Tile and Cabinet selections. I can do it all.

Industry/Entity Type

Design Agency

Contact Information for Business Card

QM Studios- Design Consultanting Residential, Commerical
Maybe a cool detail background. Wall paper print that can have some texture

Font styles to use
Serif

Colors
709dcb
34a6d7
b868aa
e667a6
f59296
85acd3
ffffff
000000
5c5c5c

Requirements
Must have
• Square or Rectangular with Rounded edges
• Name
• 218 Alder Lane, Brookfield
• (555) 014-2287
• Email
Nice to have
• Some colored edges More simples not too busy
• Pattern detail in background.
Should not have
• Not too much color

```html
<!DOCTYPE html>
<html lang="en">
<head>
<meta charset="utf-8">
<title>QM Studios — Business Card</title>
<link href="https://fonts.googleapis.com/css2?family=Cormorant+Garamond:wght@400;500&display=swap" rel="stylesheet">
<style>
  :root {
    --backdrop: #ecebe8;
    --card-white: #ffffff;
    --card-pink: #f48f97;
    --brand-pink: #f48f97;
    --ink: #3a3a3a;
    --edge-shadow: rgba(0, 0, 0, 0.14);
  }
  * { margin: 0; padding: 0; box-sizing: border-box; }
  html, body {
    width: 1200px;
    height: 1023px;
    overflow: hidden;
    background: var(--backdrop);
    font-family: "Cormorant Garamond", "Garamond", serif;
  }
  .stage {
    width: 1200px;
    height: 1023px;
    display: flex;
    flex-direction: column;
    align-items: center;
    justify-content: center;
    gap: 70px;
  }
  .card {
    width: 560px;
    height: 320px;
    border-radius: 10px;
    box-shadow: 0 10px 28px var(--edge-shadow);
    position: relative;
  }
  .card--front {
    background: var(--card-white);
    display: flex;
    align-items: center;
    justify-content: center;
  }
  .brand {
    display: flex;
    align-items: center;
    gap: 16px;
  }
  .brand__circle {
    width: 72px;
    height: 72px;
    display: block;
  }
  .brand__name {
    color: var(--brand-pink);
    font-weight: 500;
    font-size: 34px;
    letter-spacing: 0.12em;
    line-height: 1;
  }
  .card--back {
    background: var(--card-pink);
    padding: 0 56px;
    display: flex;
    flex-direction: column;
    justify-content: center;
    gap: 28px;
  }
  .contact__name {
    color: var(--ink);
    font-weight: 500;
    font-size: 34px;
    letter-spacing: 0.03em;
    line-height: 1.1;
  }
  .contact__details {
    list-style: none;
    display: flex;
    flex-direction: column;
    gap: 6px;
  }
  .contact__line {
    color: var(--ink);
    font-weight: 500;
    font-size: 18px;
    letter-spacing: 0.03em;
    line-height: 1.3;
  }
</style>
</head>
<body>
  <main class="stage">
    <section class="card card--front" aria-label="Card front">
      <div class="brand">
        <svg class="brand__circle" viewBox="0 0 72 72" aria-hidden="true">
          <circle cx="36" cy="36" r="33" fill="none" stroke="var(--brand-pink)" stroke-width="3"/>
        </svg>
        <span class="brand__name">QM Studios</span>
      </div>
    </section>
    <section class="card card--back" aria-label="Card back">
      <p class="contact__name">Mara Lowe</p>
      <ul class="contact__details">
        <li class="contact__line">hello@qmstudiosmail.com</li>
        <li class="contact__line">(555) 014-2287</li>
        <li class="contact__line">218 Alder Lane, Brookfield</li>
      </ul>
    </section>
  </main>
</body>
</html>
```